Progressive European Honey Business needs minimalistic packaging design

Hello - thank you for your interest in our brief. We are Fizzy Vixens, a London based Honey business, importing only the best honey Europe has to offer. Our values are deeply rooted with in progressive liberal values and we are looking for minimalist packaging, which reflects that.

We are looking for a design, which dimensions fit with our packaging option (Velmor Glass Jar | HEIGHT 90mm | DIAMETER 63mm). We will require a various output files (High Resolution JPEG (CMYK Colors 300 dpi) Source File Ai, PSD, PDF, Printing files (die cut, die folding) and a 3D Mockup of the packaging for use within digital commerce platforms.

We must be able to adjust the free text on the label front and it should include the following:
Brand Name
Honey type
Limited edition No. X / 100 ( X being the number of purchase i.e. 25 / 100)
EU Honey, Single Orgin (Germany)
(c) The net weight (250g)

The back must include room for additional information (again adjustable by us) and the following:
“Unsuitable for children under 12 months”
(b) The appropriate durability declaration

In total, we are looking for
a) A front label
b) A back label
c) A seal (round) including the attached bee and logo included in the Zip file.
Do note that a) & b) can also be combined into one design as long as the symmetry on the jar stays intact.

The final design should communicate modern aesthetics, high quality, that are slightly provocative and pop off the shelves.

Hi folks, sorry for the delay in completing this project, but my business partner had a leak in his house. We planned to finalise our review today, but this will have to wait until it's no longer raining in his livingroom. Our sincere apologies!

• See branding guidelines

• Must follow the branding guideline and fonts provided as attachment

```html
<!DOCTYPE html>
<html lang="en">
<head>
<meta charset="utf-8">
<title>Fizzy Vixens – Honey Labels and Seal</title>
<link href="https://fonts.googleapis.com/css2?family=Outfit:wght@600;800&family=Open+Sans:wght@400;600&family=Roboto+Condensed:wght@300;400&display=swap" rel="stylesheet">
<style>
  :root{
    --bg:#f5f5f5;
    --label:#f3f3f1;
    --orange:#e8683a;
    --orange-soft:#ec8a5f;
    --purple:#7b2d7e;
    --purple-soft:#cdb6d3;
    --ink:#1d1d1d;
    --rule:#e3b8c4;
    --bee-yellow:#f1c232;
    --bee-dark:#2b2b2b;
  }
  *{margin:0;padding:0;box-sizing:border-box}
  html,body{width:1200px;height:1169px;overflow:hidden;background:var(--bg)}
  body{position:relative;font-family:"Open Sans",sans-serif;color:var(--ink)}

  .label{position:absolute;background:var(--label);overflow:hidden}
  .label--back{left:96px;top:276px;width:289px;height:264px}
  .label--front{left:427px;top:261px;width:352px;height:321px}
  .label--info{left:809px;top:279px;width:288px;height:267px}

  .faint-mascot{position:absolute;border-radius:45%;background:radial-gradient(circle at 50% 45%,rgba(160,150,130,.16),rgba(160,150,130,.04) 70%,transparent)}
  .label--back .faint-mascot{left:65px;top:10px;width:160px;height:230px}
  .label--info .faint-mascot{left:60px;top:12px;width:165px;height:235px}

  /* back label – nutrition */
  .nutrition{position:absolute;left:88px;top:47px;width:120px;font-family:"Roboto Condensed",sans-serif;font-weight:300;font-size:7.4px;line-height:9px}
  .nutrition h2{font-family:"Open Sans",sans-serif;font-weight:600;font-size:10.5px;line-height:13px;margin-bottom:6px;border-bottom:.5px solid var(--rule);padding-bottom:2px;width:124px}
  .nutrition .serve{font-family:"Open Sans",sans-serif;font-size:8px;line-height:9.5px;display:grid;grid-template-columns:67px auto;border-bottom:.5px solid var(--rule);padding-bottom:4px;margin-bottom:3px}
  .nutrition table{width:118px;border-collapse:collapse}
  .nutrition th{font-weight:300;text-align:right;font-size:7px;padding-bottom:2px;border-bottom:.5px solid var(--rule)}
  .nutrition td{padding:0;text-align:right}
  .nutrition td:first-child{text-align:left}
  .nutrition tbody tr:last-child td{border-bottom:.5px solid var(--rule);padding-bottom:1px}
  .nutrition .ingredients{margin-top:11px;font-size:8.2px}
  .nutrition .ingredients p{margin-top:3px;font-size:7.4px;line-height:8.5px;width:124px}

  /* front label */
  .pattern{position:absolute;left:116px;top:6px;width:117px;height:172px;background:linear-gradient(180deg,var(--purple-soft),rgba(205,182,211,.5));border-radius:0 0 18px 26px}
  .brand{position:absolute;left:0;width:100%;text-align:center;font-family:"Outfit",sans-serif;font-weight:800;color:var(--orange-soft)}
  .label--front .brand{top:32px;font-size:46px;line-height:50px}
  .mascot{position:absolute;background:radial-gradient(circle at 50% 40%,var(--bee-yellow),var(--bee-dark) 75%);border-radius:46% 46% 40% 40%}
  .label--front .mascot{left:138px;top:160px;width:55px;height:61px}
  .front-rule{position:absolute;left:123px;top:219px;width:102px;height:1.5px;background:var(--purple)}
  .origin{position:absolute;top:225px;left:0;width:100%;text-align:center;font-size:8.5px;color:var(--orange-soft)}
  .honey-type{position:absolute;top:239px;left:0;width:100%;text-align:center;font-family:"Outfit",sans-serif;font-weight:600;font-size:26px;color:var(--purple)}
  .edition{position:absolute;top:271px;left:0;width:100%;text-align:center;font-family:"Outfit",sans-serif;font-weight:600;font-size:8px;color:var(--orange)}
  .weight{position:absolute;top:294px;left:0;width:100%;text-align:center;font-family:"Outfit",sans-serif;font-weight:600;font-size:9.5px}

  /* info label */
  .info{position:absolute;left:49px;top:50px;width:190px;text-align:center;font-size:9.2px;line-height:11.2px}
  .info .warning,.info .durability{font-weight:600}
  .info .durability{margin-top:11px;padding-bottom:6px;border-bottom:.5px solid var(--rule);margin-left:40px;margin-right:40px}
  .info .about{margin-top:11px;border-bottom:.5px solid var(--rule);padding-bottom:3px;margin-left:18px;margin-right:18px}
  .info .origin-note{margin-top:9px;font-size:7.5px;line-height:11.5px;color:#777}
  .info .origin-note span{color:var(--orange-soft)}

  /* seal */
  .seal{position:absolute;left:419px;top:749px;width:362px;height:362px;border-radius:50%;background:#fff}
  .seal-ring{position:absolute;inset:9px;border:2.2px solid var(--purple);border-radius:50%}
  .seal .mascot{left:125px;top:49px;width:106px;height:140px}
  .seal .brand{top:195px;font-size:48px;line-height:51px;color:var(--orange)}
</style>
</head>
<body>

  <section class="label label--back" aria-label="Back label">
    <div class="faint-mascot" role="img" aria-label="Faint crowned bee mascot illustration"></div>
    <div class="nutrition">
      <h2>Nutritional Information</h2>
      <div class="serve"><span>Serving siz</span><span>10g</span><span>Serves per pack</span><span>25</span></div>
      <table>
        <thead><tr><th></th><th>Per Serve</th><th>Per 100g</th></tr></thead>
        <tbody>
          <tr><td>Energy</td><td>xxxkj</td><td>xxxkj</td></tr>
          <tr><td>Protein</td><td>xxxg</td><td>xxg</td></tr>
          <tr><td>Fat, total</td><td>4.2g</td><td>xxg</td></tr>
          <tr><td>-Saturated</td><td>1.3g</td><td>xxg</td></tr>
          <tr><td>Carbohydrate</td><td>4.9g</td><td>xxg</td></tr>
          <tr><td>-Sugar</td><td>4.6g</td><td>xxg</td></tr>
          <tr><td>Sodium</td><td>xxxmg</td><td>xxxmg</td></tr>
        </tbody>
      </table>
      <div class="ingredients">Ingredients:
        <p>Lorem ipsum dolor sit amet, consectetuer adipiscing elit, sed diam nonummy nibh.</p>
      </div>
    </div>
  </section>

  <section class="label label--front" aria-label="Front label">
    <div class="pattern" role="img" aria-label="Dripping pattern of repeated brand name in lilac"></div>
    <div class="brand">Fizzy<br>Vixens</div>
    <div class="mascot" role="img" aria-label="Crowned bee mascot illustration"></div>
    <div class="front-rule"></div>
    <p class="origin">EU Honey, Single Orgin (Germany)</p>
    <h1 class="honey-type">HONEY TYPE</h1>
    <p class="edition">Limited edition No. X / 100</p>
    <p class="weight">250g</p>
  </section>

  <section class="label label--info" aria-label="Information label">
    <div class="faint-mascot" role="img" aria-label="Faint crowned bee mascot illustration"></div>
    <div class="info">
      <p class="warning">Unsuitable for children<br>under 12 months</p>
      <p class="durability">Best before end<br>Nov 2022</p>
      <p class="about">We are Fizzy Vixens, a London based Honey business, importing only the best honey Europe has to offer.</p>
      <p class="origin-note">EU Honey,<br>Single Orgin<br><span>(Germany)</span></p>
    </div>
  </section>

  <section class="seal" aria-label="Round seal">
    <div class="seal-ring"></div>
    <div class="mascot" role="img" aria-label="Crowned bee mascot illustration"></div>
    <div class="brand">Fizzy<br>Vixens</div>
  </section>

</body>
</html>
```